We need a business card design for a new company located in Brampton Ontario Canada. Our goal is to promote companies to use our service as an "External Program Management " firm taking their industrial product concepts " from prototype to production." We would like to use blue and yellow as our colors. Our skills include finding suppliers for prototype parts and developing them into supplying not only prototypes but the final production parts as well for our customer base.
Colin Treadway
Sales Manager
VORMEL Solutions Inc.
14 Hollowmere Lane
Brampton, Ontario L3P 8K2
Canada
Phone: 905-417-2956
Fax: 905-417-2956
website: www.vormelsolutions.example
Email: colin@vormelsolutions.example

```html
<!DOCTYPE html>
<html lang="en">
<head>
<meta charset="utf-8">
<title>VORMEL Solutions Inc. – Business Card</title>
<link href="https://fonts.googleapis.com/css2?family=Exo+2:wght@700&family=Open+Sans:ital,wght@0,400;0,600;1,400;1,700&display=swap" rel="stylesheet">
<style>
  :root {
    --bg: #d6d7d9;
    --card: #ffffff;
    --brand-blue: #1f1fc8;
    --light-blue: #4a4ae6;
    --grey: #8a8c90;
    --grey-light: #b9bbbf;
    --text-dark: #1a1a5e;
    --white: #ffffff;
  }
  * { margin: 0; padding: 0; box-sizing: border-box; }
  html, body { width: 1200px; height: 772px; overflow: hidden; }
  body {
    background: var(--bg);
    font-family: "Open Sans", Arial, sans-serif;
    position: relative;
  }
  .card {
    position: absolute;
    top: 226px;
    width: 520px;
    height: 300px;
    background: var(--card);
    box-shadow: 0 6px 18px rgba(0,0,0,0.18);
    overflow: hidden;
  }
  .card--front { left: 50px; }
  .card--back { left: 630px; }

  .wordmark {
    font-family: "Exo 2", Arial, sans-serif;
    font-weight: 700;
    color: var(--brand-blue);
    letter-spacing: 0.5px;
    white-space: nowrap;
  }
  .card--front .wordmark {
    position: absolute;
    left: 0; right: 0;
    top: 122px;
    text-align: center;
    font-size: 42px;
  }
  .card--back .wordmark {
    position: absolute;
    right: 34px;
    top: 22px;
    font-size: 28px;
  }

  .wave { position: absolute; inset: 0; width: 520px; height: 300px; }

  .holder {
    position: absolute;
    left: 36px;
    top: 60px;
  }
  .holder__name {
    font-weight: 700;
    font-style: italic;
    font-size: 16px;
    line-height: 20px;
    color: var(--text-dark);
  }
  .holder__title {
    font-style: italic;
    font-size: 13px;
    line-height: 18px;
    color: var(--grey);
  }

  .contact {
    position: absolute;
    right: 30px;
    bottom: 16px;
    list-style: none;
    text-align: right;
    color: var(--white);
    font-size: 11.5px;
    line-height: 17px;
  }
  .contact li { display: flex; justify-content: flex-end; align-items: center; gap: 6px; white-space: nowrap; }
  .contact svg { width: 10px; height: 10px; fill: var(--white); flex: none; }
</style>
</head>
<body>

<section class="card card--front" aria-label="Card front">
  <div class="wordmark">VORMEL Solutions Inc.</div>
</section>

<section class="card card--back" aria-label="Card back">
  <svg class="wave" viewBox="0 0 520 300" aria-hidden="true">
    <path d="M0,113 C110,93 200,108 270,133 C350,163 450,138 520,78 L520,90 C450,150 350,175 270,145 C200,120 110,105 0,125 Z" fill="var(--grey-light)"/>
    <path d="M0,135 C110,115 200,130 270,155 C350,185 450,160 520,100 L520,300 L0,300 Z" fill="var(--brand-blue)"/>
    <path d="M0,135 C110,115 200,130 270,155 C350,185 450,160 520,100 L520,109 C450,169 350,194 270,164 C200,139 110,124 0,144 Z" fill="var(--light-blue)"/>
  </svg>

  <div class="wordmark">VORMEL Solutions Inc.</div>

  <div class="holder">
    <div class="holder__name">Colin Treadway</div>
    <div class="holder__title">Sales Manager</div>
  </div>

  <ul class="contact">
    <li>14 Hollowmere Lane</li>
    <li>Brampton, Ontario L3P 8K2</li>
    <li>905-417-2956
      <svg viewBox="0 0 10 10" aria-label="Phone"><path d="M2,0 L4,2.5 L3,3.5 C3.6,5 5,6.4 6.5,7 L7.5,6 L10,8 L8.5,10 C4,9.5 0.5,6 0,1.5 Z"/></svg>
    </li>
    <li>905-417-2956
      <svg viewBox="0 0 10 10" aria-label="Fax"><rect x="2" y="0" width="6" height="3"/><rect x="0" y="3.5" width="10" height="4.5"/><rect x="2" y="8" width="6" height="2"/></svg>
    </li>
    <li>colin@vormelsolutions.example
      <svg viewBox="0 0 10 10" aria-label="Email"><path d="M0,2 H10 V8 H0 Z M0.8,2.6 L5,5.6 L9.2,2.6 V3.4 L5,6.4 L0.8,3.4 Z" fill-rule="evenodd"/></svg>
    </li>
    <li>www.vormelsolutions.example
      <svg viewBox="0 0 10 10" aria-label="Website"><rect x="0" y="1" width="10" height="7"/></svg>
    </li>
  </ul>
</section>

</body>
</html>
```